Business Card Design Project for Heron Lending

Hello there,

We are looking for a business card design for our new Heron Lending car financing company. We are looking for a business card that will include:

- An address
- Telephone number and extension
- Employee Name
- Employee Title
- Our logo and name clearly visible

We are including our logo with this writeup, we are looking to convey friendliness, trus and memorability. Colors and everything else is up to you.

Target Market(s)

18-34 year old males and females

Industry/Entity Type

Business

```html
<!DOCTYPE html>
<html lang="en">
<head>
<meta charset="utf-8">
<title>Heron Lending – Business Cards</title>
<link href="https://fonts.googleapis.com/css2?family=Arimo:wght@400;500&display=swap" rel="stylesheet">
<style>
  :root {
    --bg: #e9e6e2;
    --card: #ffffff;
    --navy: #1f3a6e;
    --ink: #1b1e24;
    --muted: #5a5d63;
    --rule: #2a2d33;
  }
  * { margin: 0; padding: 0; box-sizing: border-box; }
  html, body {
    width: 1200px; height: 914px; overflow: hidden;
    background: var(--bg);
    font-family: "Arimo", Arial, sans-serif;
  }
  .sheet {
    width: 1200px; height: 914px;
    display: flex; flex-direction: column;
    align-items: center; justify-content: center; gap: 44px;
  }
  .card {
    width: 700px; height: 400px;
    background: var(--card);
    box-shadow: 0 2px 10px rgba(0,0,0,.12);
    position: relative;
  }
  .wordmark {
    color: var(--navy);
    font-weight: 500;
    font-size: 34px;
    letter-spacing: 2px;
    display: flex; align-items: center; gap: 12px;
    white-space: nowrap;
  }
  .wordmark .dot {
    width: 18px; height: 18px; border-radius: 50%;
    background: var(--navy);
  }
  .card--back { display: flex; align-items: center; justify-content: center; }
  .card--back .wordmark { font-size: 40px; }

  .card--front .brand {
    position: absolute; left: 0; top: 0; width: 340px; height: 400px;
    display: flex; align-items: center; justify-content: center;
  }
  .card--front .wordmark { font-size: 30px; }
  .divider {
    position: absolute; left: 350px; top: 70px;
    width: 1.5px; height: 260px; background: var(--rule);
  }
  .details { position: absolute; left: 395px; top: 112px; color: var(--ink); }
  .employee-name { font-size: 28px; font-weight: 500; }
  .employee-title { font-size: 13px; color: var(--muted); margin-top: 4px; }
  .contact { margin-top: 52px; font-size: 18px; line-height: 1.25; }
  .contact-row { display: flex; gap: 14px; align-items: flex-start; margin-bottom: 10px; }
  .contact-row svg { flex: none; margin-top: 2px; fill: var(--navy); }
</style>
</head>
<body>
<main class="sheet">
  <section class="card card--back">
    <div class="wordmark"><span class="dot"></span>Heron Lending</div>
  </section>

  <section class="card card--front">
    <div class="brand">
      <div class="wordmark"><span class="dot"></span>Heron Lending</div>
    </div>
    <div class="divider"></div>
    <div class="details">
      <div class="employee-name">Employee Name</div>
      <div class="employee-title">Managing Director</div>
      <div class="contact">
        <div class="contact-row">
          <svg width="16" height="16" viewBox="0 0 24 24" aria-hidden="true"><path d="M6.6 10.8a15.1 15.1 0 0 0 6.6 6.6l2.2-2.2a1 1 0 0 1 1-.25 11.4 11.4 0 0 0 3.6.6 1 1 0 0 1 1 1V20a1 1 0 0 1-1 1A17 17 0 0 1 3 4a1 1 0 0 1 1-1h3.5a1 1 0 0 1 1 1c0 1.25.2 2.45.6 3.6a1 1 0 0 1-.25 1z"/></svg>
          <span>0098 7654 321</span>
        </div>
        <div class="contact-row">
          <svg width="16" height="18" viewBox="0 0 24 28" aria-hidden="true"><path d="M12 0a9 9 0 0 0-9 9c0 7 9 17 9 17s9-10 9-17a9 9 0 0 0-9-9zm0 12.5A3.5 3.5 0 1 1 12 5.5a3.5 3.5 0 0 1 0 7z"/></svg>
          <span>Address your Inc 00 Elm St<br>Millbrook, ST xxxxx</span>
        </div>
      </div>
    </div>
  </section>
</main>
</body>
</html>
```